Coffee Shop needs a fresh new menu

Hi,
I would like a new menu to be designed for our coffee shop.
We display our menu on a television screen, so would need it in a file that would allow us to continue to do so -- I have attached a photo so that you can see our current design, and how it is displayed.

I'd like something that is easy to read, if the design could have a "hipster" feel to it -- we are located at a hospital and University.

I have attached a Word file with what we would like on the menu.

Feel free to contact me if you have any questions.

Thanks,
Liv

Just A4 size will be fine, and no need to include menu 1 and menu 2 - I just put them in as an example of what we already have -- they are our printed menu's. Thanks

Hospital

```html
<!DOCTYPE html>
<html lang="en">
<head>
<meta charset="utf-8">
<title>WARD Canteen Menu</title>
<link href="https://fonts.googleapis.com/css2?family=Arimo:wght@400;700&family=Roboto+Condensed:wght@700&display=swap" rel="stylesheet">
<style>
  :root {
    --red: #e0202e;
    --red-deep: #b3121f;
    --red-light: #f04a55;
    --grey: #6d6e71;
    --grey-light: #d9d9db;
    --paper: #f2f2f3;
    --white: #ffffff;
    --ink: #333333;
  }
  * { margin: 0; padding: 0; box-sizing: border-box; }
  html, body { width: 925px; height: 1200px; overflow: hidden; }
  body {
    position: relative;
    background: radial-gradient(ellipse at 50% 55%, var(--white) 0%, var(--paper) 70%, #e6e6e8 100%);
    font-family: "Arimo", Arial, sans-serif;
    color: var(--ink);
  }
  .header-art, .footer-art { position: absolute; left: 0; display: block; }
  .header-art { top: 0; }
  .footer-art { bottom: 0; }

  .brand {
    position: absolute; left: 122px; top: 83px;
    width: 220px; height: 220px; border-radius: 50%;
    background: var(--white);
    border: 8px solid var(--red-deep);
    display: flex; align-items: center; justify-content: center;
  }
  .brand-name {
    font-family: "Roboto Condensed", Arial, sans-serif;
    font-weight: 700; font-size: 74px; color: var(--red);
    letter-spacing: 1px;
  }

  .tagline {
    position: absolute; right: 45px; top: 74px; width: 440px;
    text-align: right;
    font-family: "Roboto Condensed", Arial, sans-serif;
    font-weight: 700; font-size: 25px; line-height: 31px;
    color: var(--white);
  }

  .photo { position: absolute; border-radius: 24px; }
  .photo-coffee-mug { left: 775px; top: 210px; width: 140px; height: 125px;
    background: linear-gradient(160deg, #e6d2b4 0%, #a8663a 45%, #6e1d14 100%); }
  .photo-cappuccino { left: 500px; top: 640px; width: 140px; height: 125px;
    background: linear-gradient(160deg, #f6f3ee 0%, #e2c6a0 50%, #c99461 100%); }
  .photo-croissant { left: 655px; top: 625px; width: 250px; height: 150px;
    background: linear-gradient(160deg, #f2c45a 0%, #d08a35 55%, #9a4a1c 100%); }
  .photo-burger { left: 668px; top: 800px; width: 240px; height: 140px;
    background: linear-gradient(180deg, #d58a3a 0%, #b35a1f 35%, #6aa43a 50%, #c9321f 62%, #6a3218 80%, #c98542 100%); }
  .photo-muffins { left: 640px; top: 950px; width: 145px; height: 100px;
    background: linear-gradient(160deg, #dca46a 0%, #b06d35 60%, #7a4220 100%); }
  .photo-wrap { left: 340px; top: 1078px; width: 180px; height: 110px;
    background: linear-gradient(160deg, #efe2c8 0%, #e2c79c 45%, #c9652d 70%, #6a9e3c 100%); }
  .photo-salad { left: 660px; top: 1058px; width: 250px; height: 125px;
    background: linear-gradient(160deg, #d8a15e 0%, #7cb246 45%, #c8352a 80%, #e9e2da 100%); }

  .coffee-board {
    position: absolute; left: 44px; top: 338px; width: 445px; height: 440px;
    border-radius: 16px;
    background: linear-gradient(180deg, var(--red) 0%, #d41b29 100%);
    box-shadow: 0 4px 10px rgba(0,0,0,0.25);
    color: var(--white);
    padding-top: 6px;
    overflow: hidden;
  }
  .coffee-title {
    font-family: "Roboto Condensed", Arial, sans-serif;
    font-weight: 700; font-size: 30px; line-height: 36px;
    padding-left: 26px; margin-bottom: 8px;
  }
  .coffee-group { font-size: 15px; line-height: 19px; padding: 10px 0 11px 26px; }
  .coffee-group:first-of-type { padding-top: 0; }
  .coffee-group + .coffee-group { border-top: 2px solid var(--red-light); }
  .coffee-row { display: grid; grid-template-columns: 131px 129px auto; }
  .coffee-row.single { grid-template-columns: 131px auto; }
  .coffee-row.wide { grid-template-columns: 260px auto; }
  .coffee-row.inline { display: block; }

  .menu-section { position: absolute; }
  .section-title {
    font-family: "Roboto Condensed", Arial, sans-serif;
    font-weight: 700; font-size: 29px; line-height: 34px;
    color: var(--red);
    border-bottom: 2px solid var(--grey-light);
    padding-bottom: 6px; margin-bottom: 8px;
  }
  .menu-row { display: grid; font-size: 15px; line-height: 23.4px; }
  .breakfast { left: 510px; top: 340px; width: 300px; }
  .breakfast .menu-row { grid-template-columns: 218px auto; }
  .hot-food { left: 48px; top: 822px; width: 330px; }
  .hot-food .menu-row { grid-template-columns: 225px auto; }
  .something-light { left: 420px; top: 822px; width: 210px; }
  .something-light .menu-row { grid-template-columns: 143px auto; }
</style>
</head>
<body>

<svg class="header-art" width="925" height="340" viewBox="0 0 925 340" aria-hidden="true">
  <defs>
    <radialGradient id="headerGlow" cx="0.3" cy="0.5" r="0.8">
      <stop offset="0" stop-color="#f0414d"/>
      <stop offset="1" stop-color="#d01826"/>
    </radialGradient>
  </defs>
  <path d="M0 0H925V178Q560 150 0 262Z" fill="url(#headerGlow)"/>
  <rect x="0" y="0" width="925" height="34" fill="#c8141f"/>
  <rect x="0" y="34" width="925" height="3" fill="#9e0f19"/>
  <path d="M0 262Q560 150 925 178V200Q560 174 0 286Z" fill="#6d6e71"/>
</svg>

<div class="brand"><span class="brand-name">WARD</span></div>

<p class="tagline">Our Store inside the Hospital Food<br>Court sells: Hot Pies, Assorted<br>Pasta's, Ready -to-go Meals,<br>Quiche, and lots more!</p>

<div class="photo photo-coffee-mug" role="img" aria-label="Photo of a red mug of frothy coffee"></div>

<section class="coffee-board">
  <h2 class="coffee-title">COFFEE:</h2>
  <div class="coffee-group">
    <div class="coffee-row"><span>Latte</span><span>small $4.0</span><span>Large $4.50</span></div>
    <div class="coffee-row"><span>Cappuccino</span><span>small $4.0</span><span>Large $4.50</span></div>
    <div class="coffee-row"><span>Flat White</span><span>small $4.0</span><span>Large $4.50</span></div>
    <div class="coffee-row"><span>Long Black</span><span>small $4.0</span><span>Large $4.50</span></div>
    <div class="coffee-row"><span>Hot Chocolate</span><span>small $4.0</span><span>Large $4.50</span></div>
  </div>
  <div class="coffee-group">
    <div class="coffee-row"><span>Chai Latte</span><span>small $4.50</span><span>Large $5.0</span></div>
    <div class="coffee-row"><span>Mocha</span><span>small $4.50</span><span>Large $5.0</span></div>
    <div class="coffee-row"><span>Dirty Chai</span><span>small&nbsp; $5</span><span>Large $5.50</span></div>
  </div>
  <div class="coffee-group">
    <div class="coffee-row single"><span>Espresso</span><span>$3.50</span></div>
    <div class="coffee-row wide"><span>Short Macchiato</span><span>$4.0</span></div>
    <div class="coffee-row single"><span>Piccolo</span><span>$4.0</span></div>
    <div class="coffee-row inline">Long Macchiato $4.50</div>
  </div>
  <div class="coffee-group">
    <div>Extras</div>
    <div>Soy Milk/Lactose Free Milk/Syrups/</div>
    <div>Extra Shot/Decaf&nbsp; $0.50 extra</div>
  </div>
</section>

<div class="photo photo-cappuccino" role="img" aria-label="Photo of a cappuccino in a white cup and saucer with a spoon"></div>

<section class="menu-section breakfast">
  <h2 class="section-title">Breakfast Items</h2>
  <div class="menu-row"><span>Bacon, Egg and Cheese Roll</span><span>$6.0</span></div>
  <div class="menu-row"><span>Ham and Cheese Toastie</span><span>$5.0</span></div>
  <div class="menu-row"><span>Cheese and Tomato Toastie</span><span>$5.0</span></div>
  <div class="menu-row"><span>Ham and Cheese Croissant</span><span>$6.0</span></div>
  <div class="menu-row"><span>Cheese and Tomato Croissant</span><span>$5.50</span></div>
  <div class="menu-row"><span>Plain Croissant</span><span>$3.50</span></div>
  <div class="menu-row"><span>Hash Brown</span><span>$2.0</span></div>
  <div class="menu-row"><span>2 Piece Toast</span><span>$3.0</span></div>
  <div class="menu-row"><span>2 Piece Rasin Toast</span><span>$3.0</span></div>
</section>

<div class="photo photo-croissant" role="img" aria-label="Photo of a bacon, egg and cheese croissant"></div>
<div class="photo photo-burger" role="img" aria-label="Photo of a hamburger with lettuce, tomato and cheese"></div>
<div class="photo photo-muffins" role="img" aria-label="Photo of muffins with blueberries"></div>

<section class="menu-section hot-food">
  <h2 class="section-title">Hot Food and Sandwiches</h2>
  <div class="menu-row"><span>Pre Made Sandwiches</span><span>$6.50 - $7.50</span></div>
  <div class="menu-row"><span>Pre Made Focaccias</span><span>$8.50</span></div>
  <div class="menu-row"><span>Wraps</span><span>$7.50</span></div>
  <div class="menu-row"><span>Vegetarian Salad</span><span>$7.50</span></div>
  <div class="menu-row"><span>Meat/Seafood Salad</span><span>$9.50</span></div>
  <div class="menu-row"><span>Hot Chips</span><span>$4.50</span></div>
  <div class="menu-row"><span>Dim Sim</span><span>$1.50</span></div>
  <div class="menu-row"><span>Potato Cake</span><span>$1.50</span></div>
  <div class="menu-row"><span>Plain Hamburger</span><span>$7.50</span></div>
  <div class="menu-row"><span>Hamburger with the lot</span><span>$9.0</span></div>
  <div class="menu-row"><span>Chicken Schnitzel Burger</span><span>$8.50</span></div>
</section>

<section class="menu-section something-light">
  <h2 class="section-title">Something Light</h2>
  <div class="menu-row"><span>Mixed Yoghurts</span><span>$5.50</span></div>
  <div class="menu-row"><span>Chia Pudding</span><span>$5.50</span></div>
  <div class="menu-row"><span>Fruit Salad</span><span>$5.50</span></div>
  <div class="menu-row"><span>Bircher Muesli</span><span>$5.50</span></div>
  <div class="menu-row"><span>Protein Balls</span><span>$4.0</span></div>
  <div class="menu-row"><span>Banana Bread</span><span>$4.50</span></div>
  <div class="menu-row"><span>Muffins</span><span>$4.50</span></div>
  <div class="menu-row"><span>Slices</span><span>$4.0</span></div>
</section>

<svg class="footer-art" width="925" height="90" viewBox="0 0 925 90" aria-hidden="true">
  <path d="M0 20Q300 70 925 40V52Q300 82 0 34Z" fill="#6d6e71"/>
  <path d="M0 62Q420 98 925 46V90H0Z" fill="#e0202e"/>
</svg>

<div class="photo photo-wrap" role="img" aria-label="Photo of a chicken salad wrap"></div>
<div class="photo photo-salad" role="img" aria-label="Photo of a chicken salad in a white bowl"></div>

</body>
</html>
```